New banner design for mortgage broker

Looking for a banner design for mortgage broking company.
- need to use logo
- need to use colours from the logo
- like to use the headshot somehow.
- use slogan ' Helping to navigate your finance journey'
- include listing our services. Home Loans, Investment Loans, First Home Buyers, Self-employed Specialist, Car loans, Past Credit issues.
- call to action to get in contact today on 1300 642 917 or www.harbourfinvo.com.au
- Banner size 2.4m x 0.6m

```html
<!DOCTYPE html>
<html lang="en">
<head>
<meta charset="utf-8">
<title>Harbourfinvo – Finance Journey Banner</title>
<link href="https://fonts.googleapis.com/css2?family=Montserrat:wght@600;700&family=Roboto+Condensed:wght@800&family=Roboto:wght@400;700&display=swap" rel="stylesheet">
<style>
  :root {
    --stage: #b0b0b0;
    --purple-deep: #2f1650;
    --purple-mid: #4b2578;
    --purple-bright: #8a45cf;
    --purple-box: #5b2a8c;
    --grey-box: #58585a;
    --ink: #4a4a4c;
    --white: #ffffff;
  }
  html, body {
    margin: 0;
    width: 1200px;
    height: 592px;
    overflow: hidden;
    background: var(--stage);
  }
  .banner {
    position: absolute;
    left: 0;
    top: 146px;
    width: 1200px;
    height: 300px;
    background: var(--white);
    overflow: hidden;
    font-family: "Montserrat", sans-serif;
  }
  .banner__backdrop {
    position: absolute;
    left: 0; top: 0;
    width: 1200px; height: 222px;
    background: linear-gradient(90deg, var(--purple-deep) 0%, var(--purple-mid) 45%, #3c1d66 75%, var(--purple-mid) 100%);
  }
  .headshot {
    position: absolute;
    left: 293px; top: 27px;
    width: 122px; height: 127px;
    background: linear-gradient(180deg, #d9b98a 0%, #c9a58a 45%, #2b2d3a 78%, #1f2130 100%);
    border-radius: 60px 60px 0 0;
  }
  .slogan { margin: 0; font-weight: normal; }
  .slogan__lead {
    position: absolute;
    right: 34px; top: 34px;
    font-family: "Roboto", sans-serif;
    font-weight: 400;
    font-size: 29px;
    line-height: 1;
    letter-spacing: 5px;
    margin-right: -5px;
    color: var(--white);
    white-space: nowrap;
  }
  .slogan__main {
    position: absolute;
    right: 34px; top: 64px;
    font-family: "Roboto Condensed", sans-serif;
    font-weight: 800;
    font-size: 76px;
    line-height: 1;
    color: var(--white);
    white-space: nowrap;
  }
  .slogan__accent { color: var(--purple-bright); }
  .divider {
    position: absolute;
    left: 288px; top: 154px;
    width: 912px; height: 1px;
    background: rgba(255,255,255,0.5);
  }
  .services {
    position: absolute;
    left: 0; top: 157px;
    width: 1200px; height: 65px;
    margin: 0; padding: 0;
    list-style: none;
  }
  .service {
    position: absolute;
    top: 0; height: 65px;
    box-sizing: border-box;
    display: flex;
    align-items: center;
    justify-content: center;
    text-align: center;
    color: var(--white);
    font-weight: 600;
    font-size: 16.5px;
    line-height: 1.3;
  }
  .service--grey { background: var(--grey-box); }
  .service--purple { background: var(--purple-box); }
  .photo-frame {
    position: absolute;
    left: 0; top: 0;
    width: 320px; height: 300px;
  }
  .brand {
    position: absolute;
    left: 290px; top: 243px;
    font-family: "Montserrat", sans-serif;
    font-weight: 700;
    font-size: 19px;
    line-height: 1;
    letter-spacing: 0.3px;
    color: var(--purple-box);
    white-space: nowrap;
  }
  .contact {
    position: absolute;
    top: 239px;
    display: flex;
    align-items: center;
    gap: 9px;
    font-family: "Roboto", sans-serif;
    font-weight: 700;
    font-size: 31px;
    line-height: 1;
    color: var(--ink);
    white-space: nowrap;
  }
  .contact--phone { left: 491px; }
  .contact--web { left: 757px; }
  .contact__icon { width: 30px; height: 30px; flex: none; }
</style>
</head>
<body>
  <section class="banner">
    <div class="banner__backdrop" role="img" aria-label="Dark purple photo backdrop of a hand holding a compass"></div>

    <div class="headshot" role="img" aria-label="Headshot of the broker in a dark blazer"></div>

    <h1 class="slogan">
      <span class="slogan__lead">HELPING TO NAVIGATE</span>
      <span class="slogan__main"><span class="slogan__accent">YOUR FINANCE</span> JOURNEY</span>
    </h1>

    <div class="divider"></div>

    <ul class="services">
      <li class="service service--grey" style="left:288px;width:131px;padding-left:40px;">Home<br>Loans</li>
      <li class="service service--purple" style="left:422px;width:152px;">Investment<br>Loans</li>
      <li class="service service--grey" style="left:576px;width:157px;">First Home<br>Buyers</li>
      <li class="service service--purple" style="left:735px;width:154px;">Self-employed<br>Specialist</li>
      <li class="service service--grey" style="left:891px;width:154px;">Car<br>loans</li>
      <li class="service service--purple" style="left:1047px;width:153px;">Past Credit<br>issues</li>
    </ul>

    <svg class="photo-frame" viewBox="0 0 320 300">
      <defs>
        <clipPath id="photo-clip"><circle cx="158" cy="149" r="96"/></clipPath>
        <linearGradient id="family-tones" x1="0" y1="0" x2="0" y2="1">
          <stop offset="0" stop-color="#a9a8a4"/>
          <stop offset="0.55" stop-color="#d8d6d2"/>
          <stop offset="1" stop-color="#3e6d86"/>
        </linearGradient>
      </defs>
      <circle class="photo-frame__shadow-arc" cx="166" cy="157" r="106" fill="var(--purple-box)"/>
      <circle class="photo-frame__ring" cx="158" cy="149" r="105" fill="var(--white)"/>
      <g role="img" aria-label="Photo of a family sitting on the floor holding a house-shaped frame">
        <rect x="62" y="53" width="192" height="192" fill="url(#family-tones)" clip-path="url(#photo-clip)"/>
      </g>
    </svg>

    <div class="brand">HARBOURFINVO</div>

    <div class="contact contact--phone">
      <svg class="contact__icon" viewBox="0 0 30 30" aria-hidden="true">
        <circle cx="15" cy="15" r="15" fill="var(--purple-box)"/>
        <path d="M10.5 8.5c.8-.6 1.6-.4 2 .3l1.2 2.2c.3.6.1 1.2-.4 1.6l-.9.7c.8 1.8 2.2 3.2 4 4l.7-.9c.4-.5 1-.7 1.6-.4l2.2 1.2c.7.4.9 1.2.3 2-1 1.3-2.4 1.8-4 1.2-3.7-1.4-6.6-4.3-8-8-.6-1.6-.1-3 1.3-3.9z" fill="var(--white)"/>
      </svg>
      <span>1300 642 917</span>
    </div>

    <div class="contact contact--web">
      <svg class="contact__icon" viewBox="0 0 30 30" aria-hidden="true">
        <circle cx="15" cy="15" r="15" fill="var(--purple-box)"/>
        <circle cx="15" cy="15" r="8" fill="none" stroke="var(--white)" stroke-width="1.6"/>
        <ellipse cx="15" cy="15" rx="3.5" ry="8" fill="none" stroke="var(--white)" stroke-width="1.4"/>
        <line x1="7" y1="15" x2="23" y2="15" stroke="var(--white)" stroke-width="1.4"/>
      </svg>
      <span>www.harbourfinvo.com.au</span>
    </div>
  </section>
</body>
</html>
```